2 Independent chilean winemakers here!
La Ventisca (means door slam or slam), that is the brand for our wines (2 wines at the moment), low scale production.
We would like to have front label for our wine out of the mainstream typical french classic style. Some words to describe it: youthful yet vintage/ Osric Penwell/ brantley/ comic/ old western. Something i would wear on a t-shirt.
The text that is has to be on the label:
- La Ventisca (the brand)
-Field Blend (the type of one of the wines we have)
- 2018
- Wine of Chile.
It goes on sloping shoulder bottle, Burgundy model.
It is meant to cover a space of 3 1/4 h x 4 1/2 w inches . (or 8,5 cm height x 11cm width).
We like colours so...be creative!
I have attached the "La Ventisca" logo. We can changed it of course.
Thanks !

young drinkers (legally allowed to drink!)

• stencil

• Obvious wine things like glasses of wine, vines, grapes etc.

```html
<!DOCTYPE html>
<html lang="en">
<head>
<meta charset="utf-8">
<title>La Ventisca Field Blend 2018 – Front Label</title>
<link rel="stylesheet" href="https://fonts.googleapis.com/css2?family=Oswald:wght@400;500;600&display=swap">
<style>
  :root {
    --backdrop: #e1e1e1;
    --label-black: #111010;
    --gold: #d8b674;
    --gold-deep: #a8874c;
    --gold-shadow: #3a2f1c;
  }
  * { margin: 0; padding: 0; box-sizing: border-box; }
  html, body {
    width: 1136px;
    height: 1200px;
    overflow: hidden;
    background: var(--backdrop);
  }
  .canvas {
    position: relative;
    width: 1136px;
    height: 1200px;
  }
  .label {
    position: absolute;
    left: 119px;
    top: 80px;
    width: 898px;
    height: 1040px;
    background: var(--label-black);
    box-shadow: 0 0 0 1px #2a2a2a;
  }
  .label__frame {
    position: absolute;
    inset: 0;
    width: 898px;
    height: 1040px;
  }
  .label__text {
    position: absolute;
    left: 0;
    width: 100%;
    text-align: center;
    color: var(--gold);
    font-family: "Oswald", sans-serif;
    line-height: 1;
  }
  .label__brand {
    top: 382px;
    font-size: 54px;
    font-weight: 400;
    letter-spacing: 2px;
  }
  .label__variety {
    top: 480px;
    font-size: 104px;
    font-weight: 600;
    letter-spacing: 3px;
    text-shadow: 3px 3px 0 var(--gold-shadow);
  }
  .label__vintage {
    top: 654px;
    font-size: 42px;
    font-weight: 400;
    letter-spacing: 1px;
  }
  .label__origin {
    top: 712px;
    font-size: 30px;
    font-weight: 400;
    letter-spacing: 2px;
  }
</style>
</head>
<body>
<main class="canvas">
  <section class="label">
    <svg class="label__frame" viewBox="0 0 898 1040" xmlns="http://www.w3.org/2000/svg">
      <defs>
        <linearGradient id="filigree-tone" x1="0" y1="0" x2="1" y2="1">
          <stop offset="0" stop-color="#5e4b2a"/>
          <stop offset="1" stop-color="#3b301d"/>
        </linearGradient>
      </defs>
      <!-- border lines -->
      <rect x="22" y="22" width="854" height="996" fill="none" stroke="var(--gold)" stroke-width="4"/>
      <rect x="36" y="36" width="826" height="968" fill="none" stroke="var(--gold-deep)" stroke-width="2"/>
      <rect x="58" y="58" width="782" height="924" fill="none" stroke="var(--gold)" stroke-width="2"/>
      <!-- corner ornament areas -->
      <g role="img" aria-label="Gold filigree corner ornaments">
        <polygon points="66,66 430,66 66,430" fill="url(#filigree-tone)"/>
        <polygon points="832,66 468,66 832,430" fill="url(#filigree-tone)"/>
        <polygon points="66,974 430,974 66,610" fill="url(#filigree-tone)"/>
        <polygon points="832,974 468,974 832,610" fill="url(#filigree-tone)"/>
      </g>
      <!-- diamond frame -->
      <polygon points="449,140 830,520 449,900 68,520" fill="var(--label-black)" stroke="var(--gold)" stroke-width="4"/>
      <polygon points="449,162 808,520 449,878 90,520" fill="none" stroke="var(--gold-deep)" stroke-width="2"/>
      <!-- diamond inner ornament band -->
      <g role="img" aria-label="Gold filigree ornament inside diamond tips">
        <polygon points="449,180 530,261 368,261" fill="url(#filigree-tone)"/>
        <polygon points="449,860 530,779 368,779" fill="url(#filigree-tone)"/>
      </g>
      <!-- divider under variety -->
      <line x1="300" y1="624" x2="432" y2="624" stroke="var(--gold)" stroke-width="2"/>
      <line x1="466" y1="624" x2="598" y2="624" stroke="var(--gold)" stroke-width="2"/>
      <rect x="442" y="617" width="14" height="14" fill="var(--gold)" transform="rotate(45 449 624)"/>
    </svg>
    <p class="label__text label__brand">LA VENTISCA</p>
    <h1 class="label__text label__variety">FIELD BLEND</h1>
    <p class="label__text label__vintage">2018</p>
    <p class="label__text label__origin">WINE OF CHILE</p>
  </section>
</main>
</body>
</html>
```